GLOW NOW 14 DAY Challange

looking to make a poster that needs to be 36" wide x24"tall design graphic . Check out the added file as it is a rough draft of the material I would like it to say.

Phone number 555-014-2736 www.rbchiropractic..com

Adults aged 25-45 high income adults needing to make changes in dies and lose weight

```html
<!DOCTYPE html>
<html lang="en">
<head>
<meta charset="utf-8">
<title>GLOW NOW 14 Day Challange</title>
<link rel="stylesheet" href="https://fonts.googleapis.com/css2?family=Righteous&family=Poppins:wght@800&family=Patrick+Hand&family=Lilita+One&display=swap">
<style>
  :root{
    --navy:#2e3192;
    --navy-deep:#232a6b;
    --navy-tail:#1f2466;
    --sky:#a6dcf5;
    --ink:#222222;
    --white:#ffffff;
    --red:#ec2027;
    --arrow:#4f7fd0;
    --arrow-light:#8fb4ee;
  }
  html,body{margin:0;padding:0;overflow:hidden;background:var(--white);}
  .poster{width:1200px;height:965px;display:block;}
  .brand-name{font-family:"Lilita One",sans-serif;font-size:34px;fill:var(--navy);letter-spacing:1px;}
  .banner-title{font-family:"Righteous",sans-serif;font-size:60px;fill:none;stroke:var(--white);stroke-width:2.2px;letter-spacing:2px;}
  .hero-word{font-family:"Poppins",sans-serif;font-weight:800;font-size:300px;paint-order:stroke;stroke:var(--sky);stroke-width:22px;stroke-linejoin:round;}
  .callout{font-family:"Patrick Hand",cursive;font-size:28px;fill:var(--ink);}
  .callout-line{fill:none;stroke:var(--ink);stroke-width:1.6;stroke-dasharray:2 4;stroke-linecap:round;}
  .callout-dot{fill:var(--ink);}
  .question{font-family:"Patrick Hand",cursive;font-size:27px;fill:var(--white);letter-spacing:.5px;}
  .cta-lead{font-family:"Lilita One",sans-serif;font-size:31px;fill:var(--white);letter-spacing:1px;}
  .cta-phone{font-family:"Lilita One",sans-serif;font-size:66px;fill:var(--red);letter-spacing:1px;}
  .cta-web{font-family:"Lilita One",sans-serif;font-size:27px;fill:var(--white);letter-spacing:1px;}
  .stitch{fill:none;stroke:var(--white);stroke-width:1.2;stroke-dasharray:4 3;opacity:.8;}
</style>
</head>
<body>
<svg class="poster" viewBox="0 0 1200 965" xmlns="http://www.w3.org/2000/svg">
  <defs>
    <linearGradient id="hero-fill" x1="80" y1="0" x2="1120" y2="0" gradientUnits="userSpaceOnUse">
      <stop offset="0" stop-color="#7fc3e6"/>
      <stop offset="0.14" stop-color="#d9eef7"/>
      <stop offset="0.16" stop-color="#a9994c"/>
      <stop offset="0.30" stop-color="#b5ad6a"/>
      <stop offset="0.32" stop-color="#e59a2e"/>
      <stop offset="0.45" stop-color="#9a5a22"/>
      <stop offset="0.47" stop-color="#c4432a"/>
      <stop offset="0.60" stop-color="#8c2b2f"/>
      <stop offset="0.62" stop-color="#e6e9f0"/>
      <stop offset="0.76" stop-color="#c8505c"/>
      <stop offset="0.78" stop-color="#f0e4dc"/>
      <stop offset="1" stop-color="#d8bfae"/>
    </linearGradient>
    <radialGradient id="ring" cx="0.4" cy="0.3" r="0.8">
      <stop offset="0" stop-color="#f4f4f4"/>
      <stop offset="1" stop-color="#8d949c"/>
    </radialGradient>
    <radialGradient id="disc" cx="0.4" cy="0.3" r="0.8">
      <stop offset="0" stop-color="#6ea3e8"/>
      <stop offset="1" stop-color="#1f4fb0"/>
    </radialGradient>
    <linearGradient id="arrow-fill" x1="0" y1="0" x2="0" y2="1">
      <stop offset="0" stop-color="var(--arrow-light)"/>
      <stop offset="1" stop-color="var(--arrow)"/>
    </linearGradient>
  </defs>

  <!-- brand -->
  <g class="brand">
    <circle cx="423" cy="62" r="11" fill="var(--navy)"/>
    <text class="brand-name" x="442" y="75">RB CHIROPRACTIC</text>
  </g>

  <!-- title ribbon -->
  <g class="title-ribbon">
    <polygon points="70,90 155,90 155,190 70,190 110,140" fill="var(--navy-tail)"/>
    <polygon points="1130,90 1045,90 1045,190 1130,190 1090,140" fill="var(--navy-tail)"/>
    <polygon points="125,190 155,190 155,210" fill="#141845"/>
    <polygon points="1075,190 1045,190 1045,210" fill="#141845"/>
    <rect x="125" y="112" width="950" height="96" fill="var(--navy)"/>
    <rect class="stitch" x="133" y="119" width="934" height="82"/>
    <text class="banner-title" x="600" y="182" text-anchor="middle">GLOW NOW 14 DAY CHALLANGE</text>
  </g>

  <!-- hero word -->
  <text class="hero-word" x="88" y="552" textLength="1030" lengthAdjust="spacingAndGlyphs" fill="url(#hero-fill)"
        role="img" aria-label="Large letters GLOW NOW filled with photos: beach chair, omega 3 capsules, runner at sunset, fruits and vegetables, berries with yogurt, relaxing neck adjustment">GLOWNOW</text>

  <!-- callouts -->
  <g class="callouts">
    <text class="callout" x="248" y="262">Omega 3</text>
    <text class="callout" x="240" y="304">supplements</text>
    <path class="callout-line" d="M244 258 C222 272 228 320 262 357"/>
    <circle class="callout-dot" cx="263" cy="358" r="5"/>

    <text class="callout" x="618" y="262">Eat Fruts</text>
    <text class="callout" x="612" y="304">+ Veggies</text>
    <path class="callout-line" d="M728 292 C748 312 738 335 698 345"/>
    <circle class="callout-dot" cx="697" cy="345" r="5"/>

    <text class="callout" x="976" y="262">Chiroplactic</text>
    <text class="callout" x="980" y="304">Adjestments</text>
    <path class="callout-line" d="M975 255 C955 275 960 320 1003 345"/>
    <circle class="callout-dot" cx="1003" cy="345" r="5"/>

    <text class="callout" x="92" y="622">Lives Relax</text>
    <text class="callout" x="92" y="666">Supplements</text>
    <path class="callout-line" d="M98 556 C74 575 68 605 80 626"/>
    <circle class="callout-dot" cx="98" cy="555" r="5"/>

    <text class="callout" x="478" y="622">Vit D</text>
    <text class="callout" x="444" y="666">Supplements</text>
    <path class="callout-line" d="M536 562 C590 580 606 630 592 658"/>
    <circle class="callout-dot" cx="536" cy="562" r="5"/>

    <text class="callout" x="758" y="622">Keba Homemade</text>
    <text class="callout" x="806" y="666">Probiotic</text>
    <path class="callout-line" d="M796 556 C754 570 738 600 746 616"/>
    <circle class="callout-dot" cx="796" cy="556" r="5"/>
  </g>

  <!-- bottom band -->
  <g class="info-band">
    <rect x="0" y="700" width="1200" height="226" fill="var(--navy-deep)"/>
    <line class="stitch" x1="0" y1="709" x2="1200" y2="709"/>
    <line class="stitch" x1="0" y1="917" x2="1200" y2="917"/>

    <g class="question-icon">
      <circle cx="175" cy="800" r="67" fill="url(#ring)"/>
      <circle cx="175" cy="800" r="54" fill="url(#disc)"/>
      <text x="175" y="828" text-anchor="middle" font-family="Poppins, sans-serif" font-weight="800" font-size="78" fill="#ffffff">?</text>
    </g>

    <text class="question" x="257" y="758">Do you have Allergies ?</text>
    <text class="question" x="257" y="802">Need to lose weight?</text>
    <text class="question" x="257" y="844">Feel tired?</text>
    <text class="question" x="257" y="886">Have Neck or back Pain?</text>

    <polygon class="cta-arrow" points="556,778 628,778 628,738 700,802 628,866 628,826 556,826" fill="url(#arrow-fill)" stroke="#c9dbf7" stroke-width="1.5"/>

    <text class="cta-lead" x="720" y="765">CALL TODAY FOR DETAILS</text>
    <text class="cta-phone" x="718" y="847">555-014-2736</text>
    <text class="cta-web" x="720" y="884">WWW.RBCHIROPRACTIC..COM</text>
  </g>
</svg>
</body>
</html>
```